International Trading Company, 'KIRO' needs a Business Card

The company name is "KIRO" and it has own logo design.
I'd like to use its logo on this business card.
I need two side Business Card.
I'll look forward to your great design.
Thank you very much in advance.

Contact Information for Business Card

Company Name : Kiro Harbour Limited
Information Example
Dorian Pallister
Mobile(use icon please) : 1 (212) 555-0143
Tel(use icon please) : 1 (212) 555-0178
Email(use icon please) : dorian27@kiroharbour-mail.com
Address(use icon please) : 482 Halden Ave, New York, NY 10160, USA

```html
<!DOCTYPE html>
<html lang="en">
<head>
<meta charset="utf-8">
<title>Kiro Harbour Limited – Business Card</title>
<link rel="stylesheet" href="https://fonts.googleapis.com/css2?family=Michroma&family=Open+Sans:wght@400;600&display=swap">
<style>
  :root {
    --backdrop: #1c1c1e;
    --card: #0f0f10;
    --white: #ffffff;
    --grey: #6f6f72;
    --grey-light: #8a8a8d;
    --rule: #4a4a4d;
  }
  * { margin: 0; padding: 0; box-sizing: border-box; }
  html, body {
    width: 1200px; height: 1200px; overflow: hidden;
    background: var(--backdrop);
  }
  .canvas {
    width: 1200px; height: 1200px;
    display: flex; flex-direction: column; align-items: center; justify-content: center;
    gap: 50px;
  }
  .card {
    position: relative;
    width: 860px; height: 491px;
    background: var(--card);
    box-shadow: 0 12px 30px rgba(0,0,0,.5);
  }
  .card--front {
    display: flex; align-items: center; justify-content: center;
  }
  .wordmark {
    font-family: "Michroma", sans-serif;
    letter-spacing: 4px;
    line-height: 1;
  }
  .card--front .wordmark { font-size: 82px; color: var(--grey); }

  .holder { position: absolute; left: 62px; top: 66px; }
  .holder__name {
    font-family: "Michroma", sans-serif; font-size: 21px; letter-spacing: 5px;
    color: var(--white);
  }
  .holder__role {
    font-family: "Michroma", sans-serif; font-size: 18px; letter-spacing: 4px;
    color: var(--grey); margin-top: 4px;
  }

  .brand { position: absolute; right: 60px; top: 150px; text-align: right; }
  .card--back .wordmark { font-size: 96px; color: var(--white); }
  .brand__legal {
    font-family: "Michroma", sans-serif; font-size: 25px; letter-spacing: 4px;
    color: var(--grey); margin-top: 10px; white-space: nowrap;
  }

  .divider {
    position: absolute; left: 62px; right: 60px; top: 318px;
    height: 2px; background: var(--rule);
  }

  .contacts { position: absolute; left: 62px; top: 342px; list-style: none; }
  .contacts li {
    display: flex; align-items: center; gap: 14px;
    font-family: "Open Sans", sans-serif; font-size: 21px; color: var(--white);
    height: 34px;
  }
  .contacts svg { width: 22px; height: 22px; fill: var(--grey-light); flex: none; }

  .address {
    position: absolute; right: 60px; top: 368px;
    display: flex; align-items: center; gap: 16px;
  }
  .address__text {
    font-family: "Open Sans", sans-serif; font-size: 21px; color: var(--white);
    text-align: right; line-height: 1.45;
  }
  .address svg { width: 22px; height: 30px; fill: var(--grey-light); }
</style>
</head>
<body>
<main class="canvas">
  <section class="card card--front">
    <div class="wordmark">KIRO</div>
  </section>

  <section class="card card--back">
    <div class="holder">
      <div class="holder__name">DORIAN PALLISTER</div>
      <div class="holder__role">OWNER</div>
    </div>

    <div class="brand">
      <div class="wordmark">KIRO</div>
      <div class="brand__legal">KIRO HARBOUR LIMITED</div>
    </div>

    <div class="divider"></div>

    <ul class="contacts">
      <li>
        <svg viewBox="0 0 24 24" aria-label="Mobile"><path d="M7 1h10a2 2 0 0 1 2 2v18a2 2 0 0 1-2 2H7a2 2 0 0 1-2-2V3a2 2 0 0 1 2-2zm0 3v13h10V4H7zm5 15a1.2 1.2 0 1 0 0 2.4 1.2 1.2 0 0 0 0-2.4z"/></svg>
        1 (212) 555-0143
      </li>
      <li>
        <svg viewBox="0 0 24 24" aria-label="Telephone"><path d="M3 8c0-2 4-4 9-4s9 2 9 4v2h-5V8.5c-1-.6-2.5-.9-4-.9s-3 .3-4 .9V10H3V8zm4 3h10l3 8v2H4v-2l3-8zm5 2.5a3 3 0 1 0 0 6 3 3 0 0 0 0-6z"/></svg>
        1 (212) 555-0178
      </li>
      <li>
        <svg viewBox="0 0 24 24" aria-label="Email"><path d="M2 5h20v14H2V5zm2 2v.4l8 5.6 8-5.6V7H4zm16 2.8-8 5.6-8-5.6V17h16V9.8z"/></svg>
        dorian27@kiroharbour-mail.com
      </li>
    </ul>

    <div class="address">
      <div class="address__text">482 Halden Ave, New York<br>NY 10160, USA</div>
      <svg viewBox="0 0 22 30" aria-label="Address"><path d="M11 0C5 0 0 4.8 0 10.8 0 18.5 11 30 11 30s11-11.5 11-19.2C22 4.8 17 0 11 0zm0 15a4.3 4.3 0 1 1 0-8.6 4.3 4.3 0 0 1 0 8.6z"/></svg>
    </div>
  </section>
</main>
</body>
</html>
```